Web Design Project

Design of a complete website that has a quality and professional feel that offers video training. I have uploaded some ideas on how I am visualising the site should operate and hor the pages should interconnect. What I am NOT is a web designer, this is why I am looking for someone with the smarts and vision to make this happen, so I need someone who would like to take on this project and deliver ideas and suggestions to make this work on an automated basis. I am visualising that each page posted should be able to be edited from a back office with images, text, hyperlinks to video views and to document downloads.

Once completed and operational there would be a need for fixes, changes and adjustments as needed though I would envisage basic content would be supplied by me through the back office.

If you dont think that this project can be done within this budget, then please explain to me why and what you believe it is worth to complete. I am happy to consider all options and ideas.
Updates

Project Deadline Extended
Reason: I posted two competitions here on sketch hive at the same time, logo design and web design. This has delayed my involvement with the web design project as I needed to first settle on a logo design which has now been completed. I have not had a great deal of time available to review submitted designs and of those that have been submitted to date I am not entirely happy with. I will over the next 14 days focus on the web design element. I am wanting a complete website produced and maintained with the design being the first stage. When submitting designs, please provide an indication of if you are interested in going on to produce the complete website and your cost to do this. If you require additional information I can be contacted on tim@harbourlightlessons.com.au I will be reviewing the submitted designs so far and providing feedback on these and look forward to seeing new ideas. Tim

Target Market(s)

Mostly women with some men, probably a mix of 90/10

Industry/Entity Type

Training

Requirements
Must have
• Fast loading, user friendly, payment option my via coin vault account, the site will have a logo (currently being designed on hive), a customer database that is added to as people take up membership/purchase, needs to have auto reminders of expiring memberships and ability to create e-newsletters with their own hyperlinks to pages and tracking of read items if possible. Back office that can add delete and edit all pages adding links, photos etc.
If you have ideas please express them, I am happy to discuss any issues. I have uploaded an outline of how I am thinking this should be but I am happy to discuss your ideas.

The site needs to operate automatically with subscriptions/memberships payments provision of access to paid for elements

This project needs to be completed in a timely manner.
Nice to have
• ** Auto payment through coin vault
** auto registration and access generation
** auto reminders when membership period expires
** Ability to choose what video training is included within the membetship period
** HTML newsletters with tracking
Should not have
• The site should not look unprofessional and unappealing or take a long time to load pages, I am open to colour scheme ideas.

```html
<!DOCTYPE html>
<html lang="en">
<head>
<meta charset="utf-8">
<title>Video Training</title>
<link rel="stylesheet" href="https://fonts.googleapis.com/css2?family=Ubuntu:wght@400;500&family=Cabin+Condensed:wght@400;500&family=Arimo:wght@400;700&display=swap">
<style>
:root{
  --red:#c4000a;
  --dark:#1c1c1c;
  --hero:#353535;
  --ink:#333;
  --muted:#555;
  --panel:#efefef;
  --line:#d6d6d6;
  --footer:#3a3a3a;
  --white:#fff;
}
*{margin:0;padding:0;box-sizing:border-box}
html,body{width:1200px;height:846px;overflow:hidden;background:var(--white)}
body{position:relative;font-family:"Cabin Condensed",sans-serif;color:var(--ink)}
h1,h2{font-weight:400}
.abs{position:absolute}

.site-header{left:0;top:0;width:1200px;height:64px;
  background:repeating-linear-gradient(90deg,#222 0 2px,#151515 2px 4px)}
.brand{left:224px;top:14px;display:flex;align-items:center;gap:10px;
  font-family:"Ubuntu",sans-serif;font-size:28px;color:var(--white);letter-spacing:1px}
.brand-dot{width:14px;height:14px;border-radius:50%;background:var(--red)}
.main-nav{left:498px;top:0;height:64px;display:flex;font-family:"Ubuntu",sans-serif;
  font-size:18px;letter-spacing:2px;color:var(--white)}
.main-nav a{display:block;line-height:64px;padding:0 20px;color:inherit;text-decoration:none}
.main-nav a.active{background:#121212}

.hero{left:0;top:64px;width:1200px;height:191px;
  background:repeating-linear-gradient(90deg,#3a3a3a 0 2px,#2f2f2f 2px 4px)}
.hero-video{left:220px;top:64px;width:334px;height:191px}
.hero-still{width:334px;height:177px;
  background:linear-gradient(180deg,#e08a3a 0%,#c8602c 30%,#6a7e55 55%,#2fa3a6 75%,#2a8a8f 100%)}
.play-big{left:146px;top:72px;width:42px;height:42px;border-radius:6px;background:#222;opacity:.9}
.video-bar{left:0;top:177px;width:334px;height:14px;background:#111}
.hero-title{left:584px;top:80px;width:396px;height:46px;background:#232323;
  font-family:"Ubuntu",sans-serif;font-size:17px;font-weight:400;letter-spacing:1.6px;color:var(--white);
  line-height:46px;padding-left:28px;white-space:nowrap;overflow:hidden}
.hero-title em{font-style:normal;color:var(--red)}
.hero-text{left:586px;top:143px;width:394px;font-family:"Ubuntu",sans-serif;font-size:13px;
  line-height:16px;letter-spacing:1.1px;color:var(--white);text-align:justify}

.quote-head{left:220px;top:269px;width:178px;height:25px;background:linear-gradient(#d10010,#a40008);
  color:var(--white);font-family:"Ubuntu",sans-serif;font-size:16px;line-height:25px;padding-left:9px}
.quote-form{left:220px;top:294px;width:178px;height:208px;background:var(--panel)}
.field-label{left:6px;font-size:11.5px;color:var(--muted)}
.field{left:60px;width:111px;height:20px;border:1px solid #ccc;border-radius:4px;
  background:linear-gradient(#fff,#e4e4e4)}
.message{left:7px;top:114px;width:163px;height:55px;border:1px solid #ccc;border-radius:5px;
  background:linear-gradient(#fff,#e4e4e4);font-size:11.5px;color:var(--muted);padding:4px 9px}
.submit{left:101px;top:178px;width:68px;height:21px;border-radius:3px;background:linear-gradient(#444,#1e1e1e);
  color:var(--white);font-family:"Ubuntu",sans-serif;font-size:12px;text-align:center;line-height:21px}

.categories{left:220px;top:515px;width:177px;list-style:none;border-top:1px solid var(--line)}
.categories li{height:32px;border-bottom:1px solid var(--white);background:linear-gradient(#f3f3f3,#e6e6e6);
  font-family:"Arimo",sans-serif;font-size:11px;color:#333;line-height:32px;padding-left:16px;position:relative}
.categories li::after{content:"›";position:absolute;right:16px;color:#666}

.section-title{left:414px;font-family:"Ubuntu",sans-serif;font-size:16px;color:#333;white-space:nowrap}
.section-title em{font-style:normal;color:var(--red)}
.dots{left:414px;width:566px;border-top:1px dotted #999}
.body-copy{left:415px;width:565px;font-size:11.5px;line-height:16px;color:#333;text-align:justify}
.rule{left:470px;top:455px;width:470px;height:1px;background:linear-gradient(90deg,transparent,#ccc,transparent)}

.thumb{width:178px;height:101px}
.thumb .play{left:76px;top:41px;width:19px;height:19px;background:rgba(60,60,60,.85)}
.thumb-title{font-family:"Ubuntu",sans-serif;font-size:12.4px;color:var(--red);white-space:nowrap}
.thumb-line{width:178px;height:2px;background:#eee}

.site-footer{left:0;top:793px;width:1200px;height:53px;background:var(--footer);color:var(--white);text-align:center}
.footer-nav{margin-top:7px;font-family:"Ubuntu",sans-serif;font-size:13px}
.footer-nav a{color:inherit;text-decoration:none;margin:0 9px}
.copyright{margin-top:8px;font-size:10px}
</style>
</head>
<body>

<header class="site-header abs">
  <div class="brand abs"><span>video training</span><span class="brand-dot"></span></div>
  <nav class="main-nav abs">
    <a class="active" href="#">Home</a><a href="#">About Us</a><a href="#">Plans</a><a href="#">Blog</a><a href="#">Contact</a>
  </nav>
</header>

<section class="hero abs"></section>
<div class="hero-video abs">
  <div class="hero-still" role="img" aria-label="Video still of a coastline at sunset"></div>
  <div class="play-big abs"><svg width="42" height="42"><polygon points="16,12 16,30 30,21" fill="#fff"/></svg></div>
  <div class="video-bar abs">
    <svg width="334" height="14">
      <polygon points="5,4 5,10 10,7" fill="#fff"/>
      <text x="18" y="10" fill="#ccc" font-size="6" font-family="Arimo,sans-serif">00:30</text>
      <rect x="44" y="5" width="240" height="4" rx="2" fill="#555"/>
      <rect x="44" y="5" width="110" height="4" rx="2" fill="#ddd"/>
      <text x="290" y="10" fill="#fff" font-size="6" font-family="Arimo,sans-serif" font-weight="700">HD</text>
      <rect x="304" y="5" width="4" height="4" fill="#fff"/>
      <path d="M322 4l6 6M322 10l6-6" stroke="#fff" stroke-width="1"/>
    </svg>
  </div>
</div>
<h1 class="hero-title abs">Provide Professional <em>Video Training</em></h1>
<p class="hero-text abs">orem Ipsum is simply dummy text of the printing and typesetting industry. Lorem Ipsum has been the industry's standard dummy text ever since the 1500s, standard dummy text ever since the 1500s, when an unknown printer took a galley of type and scrambled it to make a type</p>

<h2 class="quote-head abs">» Free Quote</h2>
<form class="quote-form abs">
  <span class="field-label abs" style="top:9px">Name:</span><span class="field abs" style="top:8px"></span>
  <span class="field-label abs" style="top:35px">Email:</span><span class="field abs" style="top:34px"></span>
  <span class="field-label abs" style="top:61px">Phone:</span><span class="field abs" style="top:60px"></span>
  <span class="field-label abs" style="top:88px">Location :</span><span class="field abs" style="top:87px"></span>
  <div class="message abs">Message :</div>
  <div class="submit abs">Submit</div>
</form>

<ul class="categories abs">
  <li>Animation</li><li>Education</li><li>Entertainment</li><li>Films</li>
  <li>Music</li><li>Nature</li><li>News</li><li>Sports</li>
</ul>

<h2 class="section-title abs" style="top:265px">» Welcome To <em>Video Training</em></h2>
<div class="dots abs" style="top:294px"></div>
<p class="body-copy abs" style="top:302px">Lorem Ipsum is simply dummy text of the printing and typesetting industry. Lorem Ipsum has been the industry's standard dummy text ever since the 1500s, when an unknown printer took a galley of type and scrambled it to make a type specimen book. It has survived not only five centuries, but also the leap into electronic typesetting, remaining essentially unchanged. It was popularised in the 1960s with the release of Typeset Co sheets containing Lorem Ipsum passages, and more recently with desktop publishing software like Quill PageSetter including versions of Lorem Ipsum.</p>
<p class="body-copy abs" style="top:398px">Lorem Ipsum is simply dummy text of the printing and typesetting industry. Lorem Ipsum has been the industry's standard dummy text ever since the 1500s, when an unknown printer took a galley of type and scrambled it to make a type specimen book. It has survived not only five centuries, but also the leap into electronic typesetting.</p>
<div class="rule abs"></div>
<h2 class="section-title abs" style="top:462px">» What's New Here?</h2>
<div class="dots abs" style="top:490px"></div>

<div class="thumb abs" style="left:414px;top:502px;background:linear-gradient(#d9702c,#4a3a3a 55%,#6d8fb0)" role="img" aria-label="Rocky shore at sunset"><div class="play abs"><svg width="19" height="19"><polygon points="7,5 7,14 14,9.5" fill="#ddd"/></svg></div></div>
<div class="thumb abs" style="left:607px;top:502px;background:linear-gradient(#9a8a70,#6b5b48 50%,#8a4a3a)" role="img" aria-label="City skyline time lapse"><div class="play abs"><svg width="19" height="19"><polygon points="7,5 7,14 14,9.5" fill="#ddd"/></svg></div></div>
<div class="thumb abs" style="left:801px;top:502px;background:linear-gradient(#8a9a80,#55603e 55%,#3d4630)" role="img" aria-label="Soldier in a field"><div class="play abs"><svg width="19" height="19"><polygon points="7,5 7,14 14,9.5" fill="#ddd"/></svg></div></div>
<div class="thumb-title abs" style="left:415px;top:611px">The Arctic Light</div>
<div class="thumb-title abs" style="left:607px;top:611px">NEW YORK – Time Lapse</div>
<div class="thumb-title abs" style="left:801px;top:611px">Shadow Unit Future Soldier</div>
<div class="thumb-line abs" style="left:414px;top:633px"></div>
<div class="thumb-line abs" style="left:607px;top:633px"></div>
<div class="thumb-line abs" style="left:801px;top:633px"></div>

<div class="thumb abs" style="left:414px;top:645px;background:linear-gradient(#dfe3e3,#c8cfd0)" role="img" aria-label="Pencil sketch music video still"><div class="play abs"><svg width="19" height="19"><polygon points="7,5 7,14 14,9.5" fill="#ddd"/></svg></div></div>
<div class="thumb abs" style="left:607px;top:645px;background:linear-gradient(135deg,#2f6a6a,#8a2a3a 50%,#c9b99a)" role="img" aria-label="Abstract spinning shapes"><div class="play abs"><svg width="19" height="19"><polygon points="7,5 7,14 14,9.5" fill="#ddd"/></svg></div></div>
<div class="thumb abs" style="left:801px;top:645px;background:linear-gradient(#1e2550,#3a2f6a 60%,#1a1a30)" role="img" aria-label="Music video trailer still"><div class="play abs"><svg width="19" height="19"><polygon points="7,5 7,14 14,9.5" fill="#ddd"/></svg></div></div>
<div class="thumb-title abs" style="left:415px;top:752px">Northwave – Stay Near</div>
<div class="thumb-title abs" style="left:608px;top:752px">Future Perfect</div>
<div class="thumb-title abs" style="left:801px;top:752px">Announce Trailor</div>
<div class="thumb-line abs" style="left:414px;top:774px"></div>
<div class="thumb-line abs" style="left:607px;top:774px"></div>
<div class="thumb-line abs" style="left:801px;top:774px"></div>

<footer class="site-footer abs">
  <nav class="footer-nav"><a href="#">Home</a><a href="#">About</a><a href="#">News</a><a href="#">Blog</a><a href="#">Contact Us</a><a href="#">Jobs</a><a href="#">Privacy Policy</a><a href="#">Sitemap</a></nav>
  <p class="copyright">Copyright © 2012. All Rights Reserved by Video Training</p>
</footer>

</body>
</html>
```